Funky Business card design for starting out career counsellor - Melbourne, Australia

Hi there, I am seeking a business card design to send straight to print. I work from a psycho-spiritual framework (existential, non-dual, transpersonal) framework and was hoping for something that is modern, funky - yet has an established grounded feel to it, but pushes the edge of art and boundary. Minimal design is good.
I don't have a corporate identity other than my wordpress template at www.pathwaybrightly.com. I like the depth of the this wordpress template, with the thought provaking image. A design that aligns to the wordpress template would be awesome (but unique is okay too).
Thanks for your help :)
Contact details for card:
Marcus Halbrenn Registered Career Counsellor marcus@pathwaybrightly.com
(existential, non-dual, transpersonal)
www.pathwaybrightly.com +61 (0) 412 968 204 Melbourne CBD & Globally on Voxlink

```html
<!DOCTYPE html>
<html lang="en">
<head>
<meta charset="utf-8">
<title>Marcus Halbrenn – Business Card</title>
<link rel="stylesheet" href="https://fonts.googleapis.com/css2?family=Lato:ital,wght@0,400;0,700;1,400&display=swap">
<style>
  :root {
    --ink: #0c3b35;
    --sea-deep: #7ea4a1;
    --sea-mid: #a9c3c0;
    --sea-pale: #cfdedc;
    --glow: #ffffff;
  }
  html, body {
    margin: 0;
    padding: 0;
    width: 1200px;
    height: 741px;
    overflow: hidden;
  }
  .card {
    position: relative;
    width: 1200px;
    height: 741px;
    background: linear-gradient(90deg,
      var(--sea-deep) 0%,
      var(--sea-mid) 14%,
      var(--sea-pale) 22%,
      var(--glow) 28.5%,
      var(--sea-pale) 38%,
      var(--sea-mid) 52%,
      var(--sea-deep) 100%);
  }
  .card__text {
    position: absolute;
    inset: 0;
    width: 1200px;
    height: 741px;
  }
  .line {
    font-family: "Lato", sans-serif;
    fill: var(--ink);
    font-size: 34px;
  }
  .line--name { font-weight: 700; font-size: 41px; }
  .line--title { font-style: italic; font-size: 33px; }
  .line--approach { font-size: 31px; }
</style>
</head>
<body>
  <main class="card">
    <svg class="card__text" viewBox="0 0 1200 741" xmlns="http://www.w3.org/2000/svg">
      <text class="line line--name" x="465" y="231" transform="rotate(-27 465 231)">Marcus Halbrenn</text>
      <text class="line line--title" x="503" y="272" transform="rotate(-19.8 503 272)">Registered Career Counsellor</text>
      <text class="line line--approach" x="517" y="324" transform="rotate(-14.7 517 324)">(existential, non-dual, transpersonal)</text>
      <text class="line line--email" x="521" y="374" transform="rotate(-8.8 521 374)">marcus@pathwaybrightly.com</text>
      <text class="line line--phone" x="512" y="424">+61 (0) 412 968 204</text>
      <text class="line line--location" x="506" y="474" transform="rotate(8.8 506 474)">Melbourne CBD &amp; Globally on Voxlink</text>
      <text class="line line--web" x="499" y="515" transform="rotate(17.9 499 515)">www.pathwaybrightly.com</text>
    </svg>
  </main>
</body>
</html>
```